Business Card Design

We need a business card design for a new company based in Allen, Texas. (outside of Dallas,Texas) We offer Business Management Solutions to Entrepreneurs, as well as Corporate Businesses. Our product line offers solutions to Image, Branding, Social Media marketing, business development strategies, banking / funding solutions, just to name a few. We would like to see designs that convey strength and confidence. I have attached a sample design of our company name. Designers you may use company name as either: Vorlix or Vorlix Corporation, depending on the design layout.

Please show alternate color of Black as well.

Industry/Entity Type

Business

Contact Information for Business Card

Vorlix Corporation

2847 E. Hollowbrook Drive, STE 410
Allen, TX 75013
Office: 469.318.7742
Fax: 469.318.7743

Dr. Miles Dunworth
Business Development Director

```html
<!DOCTYPE html>
<html lang="en">
<head>
<meta charset="utf-8">
<title>Vorlix Corporation — Business Card</title>
<link href="https://fonts.googleapis.com/css2?family=Questrial&display=swap" rel="stylesheet">
<style>
  :root {
    --ink: #111314;
    --paper: #ffffff;
    --mark: #8b8e90;
  }
  html, body {
    margin: 0;
    padding: 0;
    overflow: hidden;
    background: var(--ink);
  }
  .card {
    position: relative;
    width: 1028px;
    height: 1200px;
    background: var(--ink);
    overflow: hidden;
    font-family: "Questrial", "Century Gothic", sans-serif;
  }
  .card__wedge {
    position: absolute;
    left: 0;
    top: 0;
    width: 1028px;
    height: 1200px;
  }
  .brand {
    position: absolute;
    left: 0;
    width: 100%;
    top: 175px;
    margin: 0;
    text-align: center;
    color: var(--paper);
    font-weight: 400;
    font-size: 190px;
    line-height: 1;
    letter-spacing: 2px;
  }
  .lockup {
    position: absolute;
    left: 232px;
    top: 830px;
    margin: 0;
    color: var(--mark);
    font-weight: 400;
    font-size: 76px;
    line-height: 1;
    letter-spacing: -1px;
    white-space: nowrap;
  }
  .address {
    position: absolute;
    left: 371px;
    top: 905px;
    margin: 0;
    color: var(--paper);
    font-size: 19.5px;
    white-space: nowrap;
  }
  .contact {
    position: absolute;
    top: 1097px;
    margin: 0;
    font-size: 21px;
    white-space: nowrap;
    color: var(--paper);
  }
  .contact--office { left: 76px; }
  .contact--office .contact__label { color: var(--ink); }
  .contact--fax { right: 74px; }
</style>
</head>
<body>
  <main class="card">
    <svg class="card__wedge" viewBox="0 0 1028 1200" aria-hidden="true">
      <polygon points="0,599 684,599 49,1200 0,1200" fill="var(--paper)"/>
    </svg>

    <h1 class="brand">Vorlix</h1>

    <p class="lockup">Vorlix Corporation</p>
    <p class="address">2847 E. Hollowbrook Drive, STE 410 Allen, TX 75013</p>

    <p class="contact contact--office"><span class="contact__label">Office:</span> 469.318.7742</p>
    <p class="contact contact--fax">Fax: 469.318.7743</p>
  </main>
</body>
</html>
```